Derek Hollins Business card

Hey there, I’m hoping to have a business card designed. I’m in Real estate and just switched to a new Brokerage called: The Property Quarter

The back could just be the company name maybe or whatever looks good!

I’ve attached some logos of our company and some cards my buddy had done up.

On the card:
Derek Hollins
derekhollins@mailbox-demo.com
587-214-6093
derekhollins-demo.ca

Target Market(s)

Home buyers and sellers

Industry/Entity Type

Real Estate

Contact Information for Business Card

just looking for a cool and modern design with my picture on it. I like the idea of Black and red being used.

Requirements
Must have
• all the details provided. I'm open to anything. Just want a professional looking card.

```html
<!DOCTYPE html>
<html lang="en">
<head>
<meta charset="utf-8">
<title>Derek Hollins – Business Card</title>
<link rel="stylesheet" href="https://fonts.googleapis.com/css2?family=Cinzel:wght@600;700&family=Lexend:wght@400;600;700&display=swap">
<style>
  :root {
    --page-bg: #2b2b2d;
    --card-black: #050505;
    --accent: #d8315b;
    --white: #ffffff;
    --text-soft: #f2f2f2;
    --photo-light: #e4e4e4;
    --photo-dark: #3a3f47;
  }
  * { box-sizing: border-box; margin: 0; padding: 0; }
  html, body {
    width: 1200px; height: 1200px; overflow: hidden;
    background: var(--page-bg);
  }
  .canvas {
    position: relative; width: 1200px; height: 1200px;
    display: flex; align-items: center; justify-content: center;
  }
  .business-card {
    position: relative; width: 1000px; height: 580px;
    background: var(--card-black); overflow: hidden;
  }
  .edge-stripe {
    position: absolute; left: 0; right: 0; height: 6px;
    background: var(--accent);
  }
  .edge-stripe--top { top: 14px; }
  .edge-stripe--bottom { bottom: 14px; }

  .portrait-ring {
    position: absolute; left: 70px; top: 60px;
    width: 262px; height: 262px; border-radius: 50%;
    border: 4px solid var(--accent);
    display: flex; align-items: center; justify-content: center;
  }
  .portrait {
    width: 240px; height: 240px; border-radius: 50%;
    background: linear-gradient(180deg, var(--photo-light) 0%, #cfcfcf 45%, var(--photo-dark) 100%);
  }

  .divider {
    position: absolute; left: 420px; top: 270px;
    width: 2px; height: 150px; background: var(--accent);
  }

  .agent-name {
    position: absolute; left: 462px; top: 226px;
    font-family: "Cinzel", serif; font-weight: 700;
    font-size: 38px; letter-spacing: 1px; line-height: 1;
    color: var(--white);
  }
  .agent-name .surname { color: var(--accent); }

  .accent-bar {
    position: absolute; right: 0; top: 296px;
    width: 110px; height: 38px; background: var(--white);
  }

  .contact-list {
    position: absolute; left: 466px; top: 286px;
    list-style: none;
    font-family: "Lexend", sans-serif; font-size: 20px;
    color: var(--text-soft);
  }
  .contact-item {
    display: flex; align-items: center; gap: 14px;
    height: 44px;
  }
  .contact-icon { width: 22px; height: 22px; flex: none; }

  .brand-name {
    position: absolute; right: 60px; bottom: 62px;
    display: flex; align-items: center; gap: 14px;
    font-family: "Lexend", sans-serif; font-weight: 700;
    font-size: 32px; color: var(--white); letter-spacing: 0.5px;
  }
  .brand-mark {
    width: 18px; height: 18px; background: var(--accent);
  }
</style>
</head>
<body>
<main class="canvas">
  <section class="business-card" aria-label="Derek Hollins business card">
    <div class="edge-stripe edge-stripe--top"></div>
    <div class="edge-stripe edge-stripe--bottom"></div>

    <div class="portrait-ring">
      <div class="portrait" role="img" aria-label="Portrait photo of Derek Hollins in a dark blazer"></div>
    </div>

    <div class="divider"></div>

    <h1 class="agent-name">Derek <span class="surname">Hollins</span></h1>
    <div class="accent-bar"></div>

    <ul class="contact-list">
      <li class="contact-item">
        <svg class="contact-icon" viewBox="0 0 24 24" aria-hidden="true">
          <rect x="2" y="5" width="20" height="14" rx="1.5" fill="var(--accent)"/>
          <path d="M3 6.5 L12 13 L21 6.5" fill="none" stroke="var(--card-black)" stroke-width="1.8"/>
        </svg>
        <span>derekhollins@mailbox-demo.com</span>
      </li>
      <li class="contact-item">
        <svg class="contact-icon" viewBox="0 0 24 24" aria-hidden="true">
          <path d="M6.6 2.5 L9.5 6.6 L7.8 8.8 C8.8 11.2 11 13.6 14.2 15.2 L16.3 13.5 L20.5 16.3 L19 20.2 C11 20 3.8 12.6 3.5 4.5 Z" fill="var(--accent)"/>
        </svg>
        <span>587-214-6093</span>
      </li>
      <li class="contact-item">
        <svg class="contact-icon" viewBox="0 0 24 24" aria-hidden="true">
          <circle cx="12" cy="12" r="9.5" fill="none" stroke="var(--accent)" stroke-width="2.2"/>
          <ellipse cx="12" cy="12" rx="4" ry="9.5" fill="none" stroke="var(--accent)" stroke-width="1.8"/>
          <path d="M2.5 12 H21.5 M4 7.5 H20 M4 16.5 H20" stroke="var(--accent)" stroke-width="1.6"/>
        </svg>
        <span>derekhollins-demo.ca</span>
      </li>
    </ul>

    <div class="brand-name">
      <span class="brand-mark" aria-hidden="true"></span>
      <span>The Property Quarter</span>
    </div>
  </section>
</main>
</body>
</html>
```